Business website cyber security

Full redesign of our current business website, mockup and powerpoint presentation have been provided.
Some animated elements (example: SVG with CSS) are welcome.
A detailed requirement list can also be found in the attached powerpoint
Also uploaded is the current page as a nicepage & html export. All 11 sites shall be reworked. "Branches", "Download", "Contact" and "Legal Information" are not needed .

A good example of a competitor is https://www.brantvolo.de/ this. Not in terms of colors, but in regard to website structure, animated elements and overall look.

Target Market(s)

Cyber security for the B2B market

Industry/Entity Type

IT, IT Security, banking

Coding

Coded - Design and coding required

Number of Pages Required

5+ page

Font styles to use
Other font styles liked:
• ReadexPro Regular, ReadexPro Light

Colors
0054AA
0677BA
7BADD7
CADEEF
E8F1F8

Requirements
Must have
• Modern and sleek design, corporate identity
Nice to have
• Animated elements (css svg)
Should not have
• too many colors (max 4), too fancy

```html
<!DOCTYPE html>
<html lang="de">
<head>
<meta charset="utf-8">
<title>Veltara – IT-Sicherheit</title>
<link href="https://fonts.googleapis.com/css2?family=Roboto:wght@300;400;500;700&family=Open+Sans:wght@400;600;700&display=swap" rel="stylesheet">
<style>
:root{
  --page:#0a1234;
  --page-deep:#070d28;
  --panel:#0d1a45;
  --tab:#0e1a40;
  --blue:#2f8fd8;
  --cyan:#17a8e0;
  --royal:#0b2f8e;
  --accent:#3a9be0;
  --light:#cadeef;
  --white:#ffffff;
  --muted:#c9d3e6;
}
*{margin:0;padding:0;box-sizing:border-box}
html,body{width:1200px;height:4163px;overflow:hidden}
body{background:var(--page);color:var(--white);font-family:"Open Sans",sans-serif;position:relative}
.abs{position:absolute}
.h-title{font-family:"Roboto",sans-serif;font-weight:400;text-align:center;width:1200px;left:0}
.hero{left:0;top:0;width:1200px;height:660px;background:radial-gradient(ellipse at 20% 40%,#1b3f8a 0%,rgba(10,18,52,0) 45%),radial-gradient(ellipse at 80% 55%,#16336f 0%,rgba(10,18,52,0) 50%),linear-gradient(180deg,#0b1640 0%,#132a66 50%,var(--page) 100%)}
.logo{width:101px;height:101px;border-radius:50%;background:var(--white);display:flex;align-items:center;justify-content:center;font-family:"Roboto",sans-serif;font-weight:700;color:var(--royal);font-size:19px}
.nav{top:46px;left:378px;display:flex;gap:31px;font-size:14px;font-family:"Roboto",sans-serif}
.lang{top:45px;left:1006px;display:flex;align-items:center;gap:12px;font-size:13px;font-family:"Roboto",sans-serif}
.lang i{width:22px;height:22px;border-radius:50%;background:var(--white);display:block}
.hero-title{top:188px;font-size:48px;line-height:60px}
.hero-sub{top:326px;left:150px;width:900px;text-align:center;font-size:14px;line-height:25px;color:var(--muted)}
.svc{top:693px;width:314px;height:215px;border-radius:14px;padding:30px 22px 0}
.svc .head{display:flex;gap:20px;align-items:flex-start;height:85px}
.svc .head b{font-weight:400;font-size:14px;line-height:21px;font-family:"Roboto",sans-serif;display:block;padding-top:6px}
.svc .head b:after{content:"";display:block;width:34px;height:2px;background:var(--white);margin-top:14px}
.svc p{font-size:13px;line-height:19px;text-align:justify}
.tab{left:111px;width:209px;height:58px;background:var(--tab);display:flex;align-items:center;justify-content:center;font-family:"Roboto",sans-serif;font-weight:700;font-size:15px}
.tab.on{background:var(--blue)}
.grid{left:371px;top:1085px;width:716px;height:477px;background:var(--panel);display:grid;grid-template-columns:repeat(3,1fr);grid-template-rows:1fr 1fr}
.cell{text-align:center;padding:30px 20px 0;border-right:1px solid #1a2a5e;border-bottom:1px solid #1a2a5e}
.cell h3{font-family:"Roboto",sans-serif;font-weight:700;font-size:16px;margin-top:14px}
.cell h3:after{content:"";display:block;width:30px;height:2px;background:var(--accent);margin:14px auto 18px}
.cell p{font-size:12.5px;line-height:19px;color:var(--muted)}
.wave{left:0;top:1470px;width:1200px;height:220px;background:radial-gradient(ellipse at 50% 60%,rgba(120,140,200,.25),rgba(10,18,52,0) 65%)}
.slide{top:1741px;width:315px;height:278px}
.slide span{position:absolute;bottom:38px;width:100%;text-align:center;font-family:"Roboto",sans-serif;font-size:26px}
.overlay{position:absolute;left:12px;top:12px;right:12px;bottom:12px;background:rgba(47,143,216,.82);text-align:center;padding-top:36px}
.overlay h4{font-family:"Roboto",sans-serif;font-weight:300;font-size:27px}
.overlay h4:after{content:"";display:block;width:36px;height:2px;background:var(--white);margin:14px auto 12px}
.overlay p{font-size:14px;line-height:25px}
.dots{top:2081px;left:571px;display:flex;gap:3px}
.dots i{width:11px;height:11px;border-radius:50%;background:var(--white);display:block}
.dots i.o{background:transparent;border:2px solid var(--white)}
.career{left:0;top:2160px;width:1200px;height:560px;background:radial-gradient(ellipse at 33% 55%,#1a2f6e 0%,rgba(10,18,52,0) 45%)}
.shield{left:299px;top:2229px;width:201px;height:387px}
.career-title{left:651px;top:2256px;font-family:"Roboto",sans-serif;font-weight:400;font-size:38px;color:var(--accent)}
.quote{left:651px;top:2322px;width:460px;font-family:"Roboto",sans-serif;font-size:38px;line-height:52px}
.btn{left:651px;top:2511px;width:234px;height:58px;background:var(--blue);display:flex;align-items:center;justify-content:center;font-family:"Roboto",sans-serif;font-weight:700;font-size:15px;border-radius:3px}
.partners{left:111px;top:2907px;width:976px;display:grid;grid-template-columns:repeat(5,187px);gap:24px 10px}
.partner{height:98px;border:1px solid #1e2d63;border-radius:10px;background:var(--page-deep);display:flex;align-items:center;justify-content:center;gap:8px;font-family:"Roboto",sans-serif;font-weight:500;font-size:26px}
.partner i{width:18px;height:18px;background:var(--white);display:block}
.news{top:3322px;width:316px;text-align:center}
.news .img{height:225px}
.news h4{font-size:14.5px;font-weight:700;margin-top:35px}
.news h4:after{content:"";display:block;width:30px;height:2px;background:var(--accent);margin:14px auto 14px}
.news p{font-size:13.5px;line-height:22px;color:var(--muted);padding:0 18px}
.news a{display:inline-block;margin-top:14px;font-size:13px;color:var(--accent);text-decoration:underline}
.footer{left:0;top:3820px;width:1200px;height:343px;background:var(--page-deep)}
.flogo{left:181px;top:3905px;width:172px;height:172px;border-radius:50%;background:var(--white);border:5px solid var(--blue);display:flex;align-items:center;justify-content:center;font-family:"Roboto",sans-serif;font-weight:700;color:var(--royal);font-size:30px}
.divider{top:3870px;width:1px;height:250px;background:#1d2a58}
.finfo{left:455px;width:482px;text-align:center;font-size:14px;font-weight:600}
.flinks{top:4030px;left:455px;width:482px;display:flex;justify-content:center;gap:24px;font-size:12.5px}
.social{left:979px;top:3973px;width:42px;height:42px;border-radius:50%;background:var(--blue)}
.pulse{animation:pulse 3s ease-in-out infinite}
@keyframes pulse{50%{opacity:.55}}
</style>
</head>
<body>

<div class="abs hero" role="img" aria-label="Dunkelblauer Cyber-Hintergrund mit leuchtenden Netzwerkpunkten"></div>
<div class="abs logo" style="left:111px;top:2px">Veltara</div>
<nav class="abs nav"><span>CDaaS</span><span>Security Services</span><span>Compliance</span><span>Unternehmen</span><span>Karriere</span><span>Kontakt</span></nav>
<div class="abs lang"><i></i><span>GER ▾</span></div>
<h1 class="abs h-title hero-title">Die IT-Sicherheit Ihrer &nbsp;IT-Infrastruktur<br>ist unsere Mission</h1>
<p class="abs hero-sub">sere Cybersicherheitsdienste sind rund um den Kunden konzipiert. Wir bieten eine robuste Zusammenarbeit, um die Herausforderungen Ihrer Umgebung zu verstehen und maßgeschneiderte, sichere Lösungen zu entwickeln.</p>

<section class="abs svc" style="left:111px;background:var(--blue)">
  <div class="head"><svg width="60" height="60" viewBox="0 0 60 60" fill="none" stroke="#fff" stroke-width="3"><circle cx="27" cy="28" r="20"/><path d="M7 28h40M27 8c-8 10-8 30 0 40M27 8c8 10 8 30 0 40"/><path d="M40 34l12 4v7c0 5-5 8-12 10-7-2-12-5-12-10v-7z" fill="#2f8fd8"/><path d="M35 44l4 4 7-7"/></svg><b>CDaas - Cyberverteidigung<br>als Dienstleistung</b></div>
  <p>Unser All-in-One CDaaS-Angebot, bietet eine komfortable Integration ihrer IT-Infrastruktur in eine aktive und umfassende Sicherheitslösung.</p>
</section>
<section class="abs svc" style="left:443px;background:var(--cyan)">
  <div class="head"><svg width="60" height="60" viewBox="0 0 60 60" fill="#fff"><path d="M14 24v-6a12 12 0 0124 0v6h-5v-6a7 7 0 00-14 0v6z"/><rect x="8" y="24" width="36" height="28" rx="3"/><circle cx="26" cy="36" r="4" fill="#17a8e0"/><circle cx="52" cy="22" r="4"/><circle cx="54" cy="36" r="4"/><circle cx="52" cy="50" r="4"/></svg><b>Sicherheitsdienste</b></div>
  <p>Unsere Security Services unterstützen Sie umfassend in der Planung und Umsetzung zu ihrem ganzheitlichen IT- und Informationsmanagement.</p>
</section>
<section class="abs svc" style="left:774px;background:var(--royal)">
  <div class="head"><svg width="60" height="60" viewBox="0 0 60 60" fill="none" stroke="#fff" stroke-width="4"><circle cx="30" cy="30" r="18"/><path d="M30 6v6M30 48v6M6 30h6M48 30h6M13 13l4 4M43 43l4 4M13 47l4-4M43 17l4-4"/><path d="M22 30l6 6 10-11"/></svg><b>Beachtung</b></div>
  <p>Wir unterstützen Sie rund um Ihre IT-Sicherheit auf höchstem Niveau mit ener effektiven Compliance-St</p>
</section>

<h2 class="abs h-title" style="top:1006px;font-size:30px">Vision &amp; Mission</h2>
<div class="abs tab" style="top:1085px">VISION</div>
<div class="abs tab" style="top:1166px">MISION</div>
<div class="abs tab on" style="top:1248px">PORTFOLIO</div>

<div class="abs wave pulse" role="img" aria-label="Weiche Lichtwellen aus Netzwerkpunkten"></div>
<div class="abs grid">
  <div class="cell"><svg width="44" height="46" viewBox="0 0 44 46"><path d="M22 2l18 7v13c0 11-8 19-18 22C12 41 4 33 4 22V9z" fill="#fff"/><circle cx="22" cy="23" r="9" fill="none" stroke="#0d1a45" stroke-width="3"/><path d="M18 23l3 3 5-6" stroke="#0d1a45" stroke-width="3" fill="none"/></svg><h3>IT Sicherheit</h3><p>SicherheitsinformationenEreignis Managementbetrieb &amp; Durchdringung</p></div>
  <div class="cell"><svg width="50" height="46" viewBox="0 0 50 46" fill="#fff"><circle cx="28" cy="18" r="12"/><circle cx="28" cy="18" r="5" fill="#0d1a45"/><path d="M10 34h14v4H10zM12 40h10v4H12z"/><circle cx="12" cy="14" r="6"/></svg><h3>Projektmanagement</h3><p>IT-Projektmanagement<br>Projekt für Cybersicherheit</p></div>
  <div class="cell"><svg width="46" height="46" viewBox="0 0 46 46" fill="none" stroke="#fff" stroke-width="3"><rect x="10" y="4" width="26" height="34" rx="2"/><path d="M4 42h38M16 14h14M16 21h14"/><circle cx="32" cy="32" r="6" fill="#fff"/></svg><h3>Regulatorik</h3><p>CSSF /PSF - Anforderungen<br>EZB - Anforderungen</p></div>
  <div class="cell"><svg width="48" height="46" viewBox="0 0 48 46" fill="#fff"><circle cx="18" cy="14" r="9"/><circle cx="18" cy="14" r="4" fill="#0d1a45"/><circle cx="34" cy="18" r="6"/><path d="M4 34c8-6 16-4 22 0h14v5H24c-8-3-14-2-20 3z"/></svg><h3>Betriebsdienste</h3><p>Managed Anwendungsdienste<br>Remote Services<br>Office-Suite + Cloud</p></div>
  <div class="cell"><svg width="48" height="46" viewBox="0 0 48 46" fill="#fff"><circle cx="24" cy="14" r="10"/><path d="M4 30l12-4 8 6 8-6 12 4-4 10-16 4-16-4z"/></svg><h3>Wirtschaftsanalyse</h3><p>Strategie und Lösungs - Consulting Management<br>Prozess Analyse</p></div>
  <div class="cell"><svg width="46" height="46" viewBox="0 0 46 46" fill="#fff"><path d="M23 2l20 10H3z"/><path d="M7 16h5v20H7zM17 16h5v20h-5zM26 16h5v20h-5zM35 16h5v20h-5z"/><path d="M3 38h40v5H3z"/></svg><h3>Beachtung</h3><p>Compliance-Anforderungen<br>ISMS-Risikomanagement</p></div>
</div>

<h2 class="abs h-title" style="top:1645px;font-size:30px">Branchen</h2>
<div class="abs slide" style="left:107px;background:linear-gradient(160deg,#2c5fa0,#0e2a5e 60%,#0a1a40)" role="img" aria-label="Finanzdaten-Bildschirme in blauem Licht"><span>Finanzsektor</span></div>
<div class="abs slide" style="left:443px;background:linear-gradient(160deg,#6b8db5,#3f6691)" role="img" aria-label="Arbeitsplatz mit Laptop im Büro">
  <div class="overlay"><h4>IT-service-ops</h4><p>Veranstaltungsmanagement<br>Ereignismanagement<br>Auftragsannahme<br>Zugriffsverwaltung<br>Problemmanagement</p></div>
</div>
<div class="abs slide" style="left:777px;background:linear-gradient(160deg,#4a6e92,#1e3555 60%,#0f2240)" role="img" aria-label="Fahrzeugdaten auf Monitoren im Kontrollraum"><span>Automobilindustrie</span></div>
<div class="abs dots"><i></i><i></i><i class="o"></i><i></i><i></i></div>

<div class="abs career" role="img" aria-label="Digitaler Hintergrund mit Lichtstrahlen"></div>
<div class="abs shield pulse" style="background:radial-gradient(ellipse at 50% 60%,#8d9fc4,#3d4f80 55%,rgba(10,18,52,0) 75%)" role="img" aria-label="Digitales Schutzschild mit Schlüsselloch"></div>
<h2 class="abs career-title">Arbeiten bei V.I.T.</h2>
<p class="abs quote">"Wir setzen auf Vertrauen, Zuverlässigkeit und Professionalität"</p>
<div class="abs btn">TEIL DES TEAM WERDEN</div>

<h2 class="abs h-title" style="top:2779px;font-size:38px">Produkte &amp; Partner</h2>
<p class="abs h-title" style="top:2845px;font-size:13.5px;font-family:'Open Sans',sans-serif">Wir finden für Sie die beste Lösung. Dabei entwickeln wir mit unseren individuellen Solutions ein breites Specktrum an Services.</p>
<div class="abs partners">
  <div class="partner" style="font-size:18px">Nexora 365</div>
  <div class="partner">Loglane</div>
  <div class="partner">Cloudvio</div>
  <div class="partner">Radiant QS</div>
  <div class="partner"><i></i>Fokusware</div>
  <div class="partner"><i></i>Orvantis</div>
  <div class="partner">awarely</div>
  <div class="partner" style="font-size:18px">JointShield</div>
  <div class="partner">virtania</div>
  <div class="partner">sentrio</div>
</div>

<h2 class="abs h-title" style="top:3230px;font-size:38px">Neuesten Nachrichten</h2>
<article class="abs news" style="left:107px"><div class="img" style="background:linear-gradient(135deg,#1c3c72,#4f7fb8 60%,#10254d)" role="img" aria-label="Hände auf einer Tastatur mit digitalem Schloss"></div><h4>Lorem ipsum dolor sit amet</h4><p>Sed ut perspiciatis unde omnis iste natus error sit voluptatem accusan doloremque laudantium, totam rem aperiam</p><a>LERN MEHR &nbsp;➜</a></article>
<article class="abs news" style="left:443px"><div class="img" style="background:radial-gradient(circle at 48% 52%,#2b6fb0,#0f2448 70%)" role="img" aria-label="Digitales Schloss-Symbol in einer Hand"></div><h4>Lorem ipsum dolor sit amet</h4><p>Sed ut perspiciatis unde omnis iste natus error sit voluptatem accusan doloremque laudantium, totam rem aperiam</p><a>LERN MEHR &nbsp;➜</a></article>
<article class="abs news" style="left:777px"><div class="img" style="background:linear-gradient(135deg,#3b6fa6,#1b3c6e 60%,#0d2245)" role="img" aria-label="Laptop mit Schloss-Symbol auf dem Bildschirm"></div><h4>Lorem ipsum dolor sit amet</h4><p>Sed ut perspiciatis unde omnis iste natus error sit voluptatem accusan doloremque laudantium, totam rem aperiam</p><a>LERN MEHR &nbsp;➜</a></article>

<footer class="abs footer"></footer>
<div class="abs flogo">Veltara</div>
<div class="abs divider" style="left:455px"></div>
<div class="abs divider" style="left:937px"></div>
<p class="abs finfo" style="top:3939px">Tel : &nbsp;+352 4100 27 31 - 10</p>
<p class="abs finfo" style="top:3984px">© 2022 Veltara. All Rights Reserved</p>
<div class="abs flinks"><span>Kontakt</span><span>Impressum</span><span>Datenschutz</span><span>Rechtliche Hinweise</span></div>
<div class="abs social"></div>

</body>
</html>
```